I need to refresh my meeting minutes pages (2 of them)

I have 2 pages that need to be modernized with a new look and feel. I have attached the 2 pages that need the refresh. I am okay with one page submissions as long as the winner is willing to add the second page before payment :-) Any questions please let me know. The logo on the page is not ours but a sample of what client may give us.

```html
<!DOCTYPE html>
<html lang="en">
<head>
<meta charset="utf-8">
<title>Meeting Agenda Pages</title>
<link href="https://fonts.googleapis.com/css2?family=Rubik:wght@400;500&family=Heebo:wght@400;500&display=swap" rel="stylesheet">
<style>
:root{
  --canvas:#d1d1d1;
  --panel:#ffffff;
  --blue:#1b8ad0;
  --navy:#1c3f63;
  --navy-light:#264e76;
  --logo-bg:#efefef;
  --ink:#333;
  --muted:#555;
  --line:#e2e2e2;
  --box:#f4f4f4;
  --title:#1d4a78;
}
*{box-sizing:border-box;margin:0;padding:0}
html,body{width:895px;height:1200px;overflow:hidden;background:var(--canvas);font-family:"Rubik",sans-serif;color:var(--ink)}
.page{position:absolute;left:55px;width:786px;height:530px;background:var(--panel)}
.page--agenda{top:46px}
.page--meetings{top:625px}
.sidebar{position:absolute;left:0;top:0;width:128px;height:100%;background:var(--navy);color:#fff;overflow:hidden}
.brand{height:34px;background:var(--logo-bg);display:flex;align-items:center;justify-content:center;font-family:"Heebo",sans-serif;font-weight:500;font-size:15px;color:#3a3a3a;letter-spacing:.5px}
.sec-head{background:var(--blue);height:28px;display:flex;align-items:center;padding-left:10px;font-size:8.2px;gap:4px}
.sec-head svg{width:8px;height:8px;flex:none}
.sec-head--tall{height:40px;align-items:flex-start;padding-top:8px;line-height:14px}
.sec-body{padding:0 10px;font-size:7px;line-height:13px;display:flex;flex-direction:column;justify-content:center}
.tags{display:flex;gap:0;margin-top:6px;margin-left:-4px}
.tags span{padding:2px 6px;font-size:7px}
.tags .on{background:var(--navy-light)}
.acc{height:26px;display:flex;align-items:center;justify-content:space-between;padding:0 16px 0 18px;font-size:8.2px}
.acc.head{background:var(--blue);height:28px}
.acc.year{font-size:7.5px;border-bottom:1px solid #2a4d72}
.mt{height:39.2px;padding:6px 0 0 18px;font-size:7.5px;line-height:13.5px;border-bottom:1px solid #24486d}
.mt.active{background:#244b73}
.mt svg{width:6px;height:6px;margin-right:3px;vertical-align:-.5px}
.search{position:absolute;left:147px;top:10px;width:246px;height:24px;border:1px solid var(--line);font-size:7.6px;color:#666;display:flex;align-items:center;justify-content:space-between;padding:0 10px}
.search svg{width:9px;height:9px}
.topnav{position:absolute;top:16px;right:26px;display:flex;gap:14px;font-size:7.6px;color:#444}
.topnav a{color:inherit;text-decoration:none;display:flex;align-items:center;gap:3px}
.topnav a.current{color:var(--blue)}
.topnav svg{width:7px;height:7px}
.btn{position:absolute;top:56px;width:19px;height:21px;background:var(--navy);display:flex;align-items:center;justify-content:center}
.btn svg{width:8px;height:8px}
.btn--ghost{background:#fff;border:1px solid #eee;width:25px}
.share{position:absolute;top:56px;right:27px;width:27px;height:21px;border:1px solid #eee;display:flex;align-items:center;justify-content:center}
.share svg{width:12px;height:10px}
.frame{position:absolute;left:147px;top:95px;width:613px;border:1px dashed var(--line)}
.card{position:absolute;left:6px;top:6px;right:6px;bottom:6px;background:var(--box)}
.photo{position:absolute;left:10px;top:11px;width:279px;height:243px}
.photo--agent{background:linear-gradient(120deg,#9aa6ad 0%,#e9ece9 35%,#c9b6a8 55%,#4d6f66 85%)}
.photo--room{background:linear-gradient(160deg,#b6bccd 0%,#d9d9df 35%,#6b5a4f 70%,#2d2b2d 100%)}
.facts{position:absolute;left:316px;top:30px;font-size:10px}
.facts dl{display:grid;grid-template-columns:105px 160px;row-gap:15px;align-items:baseline}
.facts dt{color:#222}
.facts dd{font-size:8.7px;color:var(--muted)}
.file{position:absolute;left:316px;top:148px;width:269px;height:104px;background:#fff;border:1px dashed #ddd;display:flex;align-items:center;justify-content:center;font-size:8.7px;color:#444;gap:4px}
.file svg{width:8px;height:8px}
.meeting{position:absolute;left:315px;top:35px;width:270px}
.meeting h2{font-weight:500;font-size:13px;color:var(--title);margin-bottom:10px}
.meeting .row{font-size:10.5px;color:#333;display:flex;align-items:center;gap:4px;height:20px}
.meeting .row svg{width:9px;height:9px;flex:none}
.meeting p{margin-top:8px;font-size:8.6px;line-height:16px;color:var(--muted)}
.action{position:absolute;top:257px;width:187px;height:128px;background:#fff;border:1px dashed #ddd;display:flex;align-items:center;justify-content:center;gap:4px;font-size:8.8px;color:#444}
.action svg{width:9px;height:9px}
</style>
</head>
<body>

<section class="page page--agenda">
  <nav class="sidebar">
    <div class="brand">NVSD</div>
    <div class="sec-head"><svg viewBox="0 0 10 10"><circle cx="5" cy="5" r="4" fill="#fff"/></svg>*R* Welcome</div>
    <div class="sec-body" style="height:30px">Wireless Access For Guests</div>
    <div class="sec-head"><svg viewBox="0 0 10 10"><circle cx="5" cy="5" r="4" fill="none" stroke="#fff" stroke-width="1.5"/></svg>*R* Call To Order</div>
    <div class="sec-body" style="height:45px;line-height:17px">Pledge Of Allegiance<br>Roll Call</div>
    <div class="sec-head"><svg viewBox="0 0 10 10"><circle cx="5" cy="5" r="4.5" fill="#fff"/><path d="M5 2.3l.8 1.8 1.9.2-1.4 1.3.4 1.9L5 6.5 3.3 7.5l.4-1.9-1.4-1.3 1.9-.2z" fill="#1b8ad0"/></svg>Riverton Proud</div>
    <div class="sec-body" style="height:63px;line-height:15px">Lakeside Hockey Coach<br>Teaching Professions- Educator<br>&nbsp;Rising State Competition</div>
    <div class="sec-head sec-head--tall"><svg viewBox="0 0 10 10" style="margin-top:3px"><rect x="1" y="1" width="6" height="8" fill="none" stroke="#fff"/><rect x="4" y="3" width="5" height="6" fill="#fff"/></svg>*R* Information To The<br>Board</div>
    <div class="sec-body" style="height:69px">Superintendent-ACES/PAGE/<br>First Step
      <div class="tags"><span>ACES</span><span class="on">PAGE</span><span>FIRST STEP</span></div>
    </div>
    <div class="sec-head"><svg viewBox="0 0 10 10"><circle cx="3" cy="3" r="2" fill="#fff"/><circle cx="7" cy="3" r="2" fill="#fff"/><rect x="0.5" y="5.5" width="9" height="4" rx="2" fill="#fff"/></svg>*R* Public Participation</div>
    <div class="sec-body" style="height:57px">Invitation for Public Comments<br>Concerining Agenda Items<br>TO Be Adopted This Evening</div>
    <div class="sec-head"><svg viewBox="0 0 10 10"><rect x="1" y="1" width="8" height="8" rx="1" fill="#fff"/><path d="M3 7l1-2 3-3 1 1-3 3z" fill="#1b8ad0"/></svg>Adoption of Amendments</div>
    <div class="sec-body" style="height:51px">Resolution 2025-04-148<br>Adoption of Amendment(s)<br>and/or</div>
  </nav>

  <div class="search">Search Agenda<svg viewBox="0 0 10 10"><circle cx="4.3" cy="4.3" r="3.3" fill="none" stroke="#333"/><path d="M6.8 6.8L9 9" stroke="#333"/></svg></div>
  <div class="topnav">
    <a><svg viewBox="0 0 8 8"><rect width="8" height="2" fill="#1b8ad0"/><rect y="3" width="8" height="2" fill="#1b8ad0"/><rect y="6" width="8" height="2" fill="#1b8ad0"/></svg>Featured</a>
    <a><svg viewBox="0 0 8 8"><ellipse cx="4" cy="3.5" rx="3.5" ry="2.5" fill="none" stroke="#1b8ad0"/></svg>Meetings</a>
    <a class="current"><svg viewBox="0 0 8 8"><rect x=".5" y="1" width="7" height="6.5" fill="none" stroke="#1b8ad0"/><rect x=".5" y="1" width="7" height="2" fill="#1b8ad0"/></svg>Agenda</a>
    <a><svg viewBox="0 0 8 8"><path d="M1 1h6v3c0 2-3 3.5-3 3.5S1 6 1 4z" fill="#1d4a78"/></svg>Policies</a>
  </div>

  <span class="btn" style="left:148px"><svg viewBox="0 0 8 8"><path d="M5.5 1L2.5 4l3 3" fill="none" stroke="#fff" stroke-width="1.3"/></svg></span>
  <span class="btn btn--ghost" style="left:172px"><svg viewBox="0 0 10 10"><rect x="2.5" y="1" width="5" height="3" fill="#1d4a78"/><rect x="1" y="4" width="8" height="3.5" rx=".6" fill="#1d4a78"/><rect x="2.5" y="6.5" width="5" height="2.5" fill="#fff" stroke="#1d4a78" stroke-width=".8"/></svg></span>
  <span class="btn" style="left:204px"><svg viewBox="0 0 8 8"><path d="M2.5 1l3 3-3 3" fill="none" stroke="#fff" stroke-width="1.3"/></svg></span>
  <span class="share"><svg viewBox="0 0 12 10"><path d="M7 0l5 4-5 4V5.5C3.5 5.5 1.5 6.5 0 9c.5-4 3-6 7-6.5z" fill="#1b8ad0"/></svg></span>

  <div class="frame" style="height:276px">
    <div class="card">
      <div class="photo photo--agent" role="img" aria-label="Photo of a smiling support agent wearing a headset at a computer"></div>
      <div class="facts">
        <dl>
          <dt>Meeting:</dt><dd>Apr 10,2025-regular Meeting Agenda</dd>
          <dt>Category:</dt><dd>*R* Information To The Board</dd>
          <dt>Subject:</dt><dd>Page</dd>
          <dt>Tybe:</dt><dd></dd>
        </dl>
      </div>
      <div class="file"><svg viewBox="0 0 8 8"><rect x=".5" y=".5" width="7" height="7" fill="none" stroke="#1b8ad0"/><rect x="2" y=".5" width="4" height="2.5" fill="#1b8ad0"/><rect x="2" y="5" width="4" height="2.5" fill="#1b8ad0"/></svg>2025-04-10- Riverton Proud -Page(1).Pdf (40 KB)</div>
    </div>
  </div>
</section>

<section class="page page--meetings">
  <nav class="sidebar">
    <div class="brand">NVSD</div>
    <div class="acc head">Featured<span>+</span></div>
    <div class="acc year">2025<span>-</span></div>
    <div class="mt"><svg viewBox="0 0 8 8"><path d="M4 0l1.2 2.6 2.8.3-2.1 1.9.6 2.8L4 6.2 1.5 7.6l.6-2.8L0 2.9l2.8-.3z" fill="#fff"/></svg>May 1,2025 (Thu)<br>Regular Meeting &nbsp;Agenda</div>
    <div class="mt active"><svg viewBox="0 0 8 8"><rect x=".5" y="1" width="7" height="6.5" fill="none" stroke="#fff"/><rect x=".5" y="1" width="7" height="2" fill="#fff"/></svg>Apr10,2025 (Wed)<br>Regular Meeting &nbsp;Agenda</div>
    <div class="mt"><svg viewBox="0 0 8 8"><rect x=".5" y="1" width="7" height="6.5" fill="none" stroke="#fff"/><rect x=".5" y="1" width="7" height="2" fill="#fff"/></svg>Apr 15,2025 (Sun)<br>Regular Meeting &nbsp;Agenda</div>
    <div class="mt"><svg viewBox="0 0 8 8"><rect x=".5" y="1" width="7" height="6.5" fill="none" stroke="#fff"/><rect x=".5" y="1" width="7" height="2" fill="#fff"/></svg>Jun 1,2025 (Thu)<br>Regular Meeting &nbsp;Agenda</div>
    <div class="mt"><svg viewBox="0 0 8 8"><rect x=".5" y="1" width="7" height="6.5" fill="none" stroke="#fff"/><rect x=".5" y="1" width="7" height="2" fill="#fff"/></svg>Jun 20,2025 (Wed)<br>Regular Meeting &nbsp;Agenda</div>
    <div class="mt"><svg viewBox="0 0 8 8"><rect x=".5" y="1" width="7" height="6.5" fill="none" stroke="#fff"/><rect x=".5" y="1" width="7" height="2" fill="#fff"/></svg>May 1,2025 (Thu)<br>Regular Meeting &nbsp;Agenda</div>
    <div class="mt"><svg viewBox="0 0 8 8"><rect x=".5" y="1" width="7" height="6.5" fill="none" stroke="#fff"/><rect x=".5" y="1" width="7" height="2" fill="#fff"/></svg>Aug 1,2025 (Thu)<br>Regular Meeting &nbsp;Agenda</div>
    <div class="mt"><svg viewBox="0 0 8 8"><rect x=".5" y="1" width="7" height="6.5" fill="none" stroke="#fff"/><rect x=".5" y="1" width="7" height="2" fill="#fff"/></svg>Sep 15,2025 (Mon)<br>Regular Meeting &nbsp;Agenda</div>
    <div class="mt"><svg viewBox="0 0 8 8"><rect x=".5" y="1" width="7" height="6.5" fill="none" stroke="#fff"/><rect x=".5" y="1" width="7" height="2" fill="#fff"/></svg>Oct 1,2025 (Thu)<br>Regular Meeting &nbsp;Agenda</div>
    <div class="mt"><svg viewBox="0 0 8 8"><rect x=".5" y="1" width="7" height="6.5" fill="none" stroke="#fff"/><rect x=".5" y="1" width="7" height="2" fill="#fff"/></svg>Oct22,2025 (Tue)<br>Regular Meeting &nbsp;Agenda</div>
    <div class="mt"><svg viewBox="0 0 8 8"><rect x=".5" y="1" width="7" height="6.5" fill="none" stroke="#fff"/><rect x=".5" y="1" width="7" height="2" fill="#fff"/></svg>Jul 13,2025 (Fri)<br>Regular Meeting &nbsp;Agenda</div>
  </nav>

  <div class="search">Search Meetings<svg viewBox="0 0 10 10"><circle cx="4.3" cy="4.3" r="3.3" fill="none" stroke="#333"/><path d="M6.8 6.8L9 9" stroke="#333"/></svg></div>
  <div class="topnav">
    <a><svg viewBox="0 0 8 8"><rect width="8" height="2" fill="#1b8ad0"/><rect y="3" width="8" height="2" fill="#1b8ad0"/><rect y="6" width="8" height="2" fill="#1b8ad0"/></svg>Featured</a>
    <a class="current"><svg viewBox="0 0 8 8"><ellipse cx="4" cy="3.5" rx="3.5" ry="2.5" fill="none" stroke="#1b8ad0"/></svg>Meetings</a>
    <a><svg viewBox="0 0 8 8"><rect x=".5" y="1" width="7" height="6.5" fill="none" stroke="#1b8ad0"/><rect x=".5" y="1" width="7" height="2" fill="#1b8ad0"/></svg>Agenda</a>
    <a><svg viewBox="0 0 8 8"><path d="M1 1h6v3c0 2-3 3.5-3 3.5S1 6 1 4z" fill="#1d4a78"/></svg>Policies</a>
  </div>

  <span class="btn" style="left:148px"><svg viewBox="0 0 8 8"><path d="M5.5 1L2.5 4l3 3" fill="none" stroke="#fff" stroke-width="1.3"/></svg></span>
  <span class="btn" style="left:172px"><svg viewBox="0 0 8 8"><path d="M2.5 1l3 3-3 3" fill="none" stroke="#fff" stroke-width="1.3"/></svg></span>
  <span class="share"><svg viewBox="0 0 12 10"><path d="M7 0l5 4-5 4V5.5C3.5 5.5 1.5 6.5 0 9c.5-4 3-6 7-6.5z" fill="#1b8ad0"/></svg></span>

  <div class="frame" style="height:417px">
    <div class="card">
      <div class="photo photo--room" role="img" aria-label="Photo of colleagues at a table joining a video conference on a wall screen"></div>
      <div class="meeting">
        <h2>REGULAR MEETING AGENDA</h2>
        <div class="row"><svg viewBox="0 0 8 8"><rect x=".5" y="1" width="7" height="6.5" fill="none" stroke="#1b8ad0"/><rect x=".5" y="1" width="7" height="2" fill="#1b8ad0"/></svg>Thursday,april 24,2025</div>
        <div class="row"><svg viewBox="0 0 8 8"><path d="M4 0C2.3 0 1 1.3 1 3c0 2.2 3 5 3 5s3-2.8 3-5C7 1.3 5.7 0 4 0z" fill="#1b8ad0"/><circle cx="4" cy="3" r="1" fill="#f4f4f4"/></svg>Lakeside High School Media center</div>
        <div class="row">1800 North Maple Road Riverton, Ohio 44000</div>
        <div class="row"><svg viewBox="0 0 8 8"><circle cx="4" cy="4" r="3.3" fill="none" stroke="#1b8ad0" stroke-width="1.2"/><path d="M4 2v2h1.5" stroke="#1b8ad0" fill="none"/></svg>6:00 P.M</div>
        <p>This Meeting Is A Meeting Of The Board of Education In Public For The Purpose of Conducting The District 's Businesss.there Is A Time For Time Public Particiation Dutinmg The Meeting as Indicated In The Agenda</p>
      </div>
      <div class="action" style="left:10px"><svg viewBox="0 0 9 9"><rect y="1" width="1.5" height="1.5" fill="#1b8ad0"/><rect x="2.5" y="1" width="6.5" height="1.5" fill="#1b8ad0"/><rect y="4" width="1.5" height="1.5" fill="#1b8ad0"/><rect x="2.5" y="4" width="6.5" height="1.5" fill="#1b8ad0"/><rect y="7" width="1.5" height="1.5" fill="#1b8ad0"/><rect x="2.5" y="7" width="6.5" height="1.5" fill="#1b8ad0"/></svg>View The Agenda</div>
      <div class="action" style="left:206px"><svg viewBox="0 0 9 9"><path d="M1.5.5h4l2 2v6h-6z" fill="none" stroke="#1b8ad0"/><path d="M5.5.5v2h2" fill="none" stroke="#1b8ad0"/></svg>Download Agenda is PDF</div>
      <div class="action" style="left:402px"><svg viewBox="0 0 10 10"><rect x="2.5" y="1" width="5" height="3" fill="#1b8ad0"/><rect x="1" y="4" width="8" height="3.5" rx=".6" fill="#1b8ad0"/><rect x="2.5" y="6.5" width="5" height="2.5" fill="#fff" stroke="#1b8ad0" stroke-width=".8"/></svg>Print The Agenda</div>
    </div>
  </div>
</section>

</body>
</html>
```